Design Business Card (Group Companies)

Hi Contenders,

PLEASE NOTE I NEED ALL LOGOS ON ONE CARD!!!!!!!!!!!!!!!!!!!!

I have multiple Businesses and would like to have a business card that will showcase all my brands and my business details.

I have attached a logo of each business and would like them to be included on the business card in some way.

Open to your ideas

```html
<!DOCTYPE html>
<html lang="en">
<head>
<meta charset="utf-8">
<title>Group Companies Business Card</title>
<link href="https://fonts.googleapis.com/css2?family=Montserrat:wght@400;600;800&display=swap" rel="stylesheet">
<style>
  :root {
    --stage: #d9d6d2;
    --card: #0b0b0b;
    --ink: #ffffff;
    --muted: #d8d8d8;
    --ghost: rgba(255,255,255,0.06);
    --rule: rgba(255,255,255,0.55);
  }
  * { margin: 0; padding: 0; box-sizing: border-box; }
  html, body { width: 1200px; height: 900px; overflow: hidden; }
  body {
    background: var(--stage);
    font-family: "Montserrat", Arial, sans-serif;
    color: var(--ink);
    position: relative;
  }
  .card {
    position: absolute;
    left: 280px;
    width: 640px;
    height: 366px;
    background: var(--card);
    overflow: hidden;
    box-shadow: 0 10px 30px rgba(0,0,0,0.35);
  }
  .card--front { top: 70px; }
  .card--back { top: 464px; }

  .ghost-name {
    position: absolute;
    left: 50%; top: 50%;
    transform: translate(-50%, -50%);
    font-weight: 800; font-size: 60px;
    color: var(--ghost);
    white-space: nowrap;
  }

  .brand-grid {
    position: absolute; inset: 0;
    display: grid;
    grid-template-columns: 1fr 1fr;
    grid-template-rows: 1fr 1fr;
    padding: 60px 50px;
    align-items: center;
  }
  .brand {
    display: flex; align-items: center; gap: 10px;
    font-weight: 800; font-size: 30px; letter-spacing: -0.5px;
    color: var(--ink);
    position: relative;
  }
  .brand .square {
    width: 32px; height: 32px; background: var(--ink);
    flex: none;
  }
  .brand--right { justify-self: end; }

  .contact {
    position: absolute; left: 44px; top: 120px;
    width: 260px;
  }
  .contact__name {
    font-weight: 800; font-size: 22px; letter-spacing: 1px;
    text-transform: uppercase;
    padding-bottom: 6px;
    border-bottom: 1.5px solid var(--rule);
    display: inline-block;
  }
  .contact__role {
    font-size: 11px; letter-spacing: 1.5px; color: var(--muted);
    margin-top: 6px; text-transform: uppercase;
  }
  .contact__address {
    font-size: 15px; line-height: 1.35; margin-top: 22px; color: var(--muted);
  }
  .contact__line {
    display: flex; align-items: center; gap: 12px;
    font-size: 15px; color: var(--muted); margin-top: 12px;
  }
  .contact__line svg { width: 16px; height: 16px; flex: none; fill: var(--ink); }

  .divider {
    position: absolute; left: 360px; top: 0; bottom: 0;
    width: 1px; background: var(--rule);
  }
  .globe {
    position: absolute; left: 350px; top: 168px;
    width: 21px; height: 21px;
  }
  .web-list {
    position: absolute; left: 392px; top: 70px;
    list-style: none;
    font-size: 15px; line-height: 2.05; color: var(--muted);
  }
</style>
</head>
<body>

<section class="card card--front" aria-label="Card front">
  <div class="ghost-name" aria-hidden="true">bidyard365</div>
  <div class="brand-grid">
    <div class="brand">bidyard365</div>
    <div class="brand brand--right"><span class="square"></span>RoadLease</div>
    <div class="brand">Keel Path Freight</div>
    <div class="brand brand--right"><span class="square"></span>FundPoint</div>
  </div>
</section>

<section class="card card--back" aria-label="Card back">
  <div class="ghost-name" aria-hidden="true">bidyard365</div>

  <div class="contact">
    <h1 class="contact__name">Marin Osler</h1>
    <p class="contact__role">Owner &amp; CEO</p>
    <p class="contact__address">48 Harbour Lane,<br>Port Vale, QX-2210</p>
    <p class="contact__line">
      <svg viewBox="0 0 24 24" aria-hidden="true"><path d="M6.6 10.8a15.1 15.1 0 0 0 6.6 6.6l2.2-2.2c.3-.3.7-.4 1-.2 1.1.4 2.3.6 3.6.6.6 0 1 .4 1 1V20c0 .6-.4 1-1 1A17 17 0 0 1 3 4c0-.6.4-1 1-1h3.5c.6 0 1 .4 1 1 0 1.3.2 2.5.6 3.6.1.3 0 .7-.2 1z"/></svg>
      000 9876 5432
    </p>
    <p class="contact__line">
      <svg viewBox="0 0 24 24" aria-hidden="true"><path d="M2 5h20v14H2z" /><path d="M2 5l10 8 10-8" fill="none" stroke="#0b0b0b" stroke-width="2"/></svg>
      hello@mailbox.com
    </p>
  </div>

  <div class="divider"></div>
  <svg class="globe" viewBox="0 0 24 24" aria-hidden="true">
    <circle cx="12" cy="12" r="11" fill="#0b0b0b"/>
    <circle cx="12" cy="12" r="10" fill="#ffffff"/>
    <g fill="none" stroke="#0b0b0b" stroke-width="1.4">
      <ellipse cx="12" cy="12" rx="4.5" ry="10"/>
      <line x1="2" y1="12" x2="22" y2="12"/>
      <line x1="12" y1="2" x2="12" y2="22"/>
    </g>
  </svg>

  <ul class="web-list">
    <li>www.bidyard365.com.au</li>
    <li>www.roadlease.com.au</li>
    <li>www.keelpath.com.au</li>
    <li>www.fundpoint.com.au</li>
  </ul>
</section>

</body>
</html>
```